Welcome Booklet for Plastic Surgery Patients

I need a welcome booklet for a plastic surgery office. We already have the content and a logo, we just need help putting together a design for the booklet. The book details the types of procedures offered by the doctor (Larisse Whitcombe M.D). Attached is a booklet from another doctor as a reference point (Dorvenna Plastic Surgery).
We would like it to be mainly white, gray, black with a little bit of pink as a reflection of the doctors work with Breast Cancer.

Target Market(s)

It is meant to be informative for women seeking Breast Reconstruction who have been diagnosed with breast cancer.

Industry/Entity Type

Plastic

Font styles to use
Other font styles liked:
• century gothic

Colors
7f7f7f
ffffff
1b1b1b
eda3c7

Requirements
Must have
• - Address shown on the back page (we have two locations) -
• 718 S Haverlin Suite 206 Beverly Hills CA 90211
• 41872 Pellworth Street Suite 205 Torrance CA 90503
• - The personal picture of Dr. Whitcombe needs to be on the welcome page
• - Pages 3-7 should have breast reconstruction at the top
• - Page 8 should have face at the top
• - Page 9 Should have body at the top
• - Attached is the image we want for the cover
Nice to have
• -The names of the procedures to stand out
• - For the most part we want a very clean look
• - The logo has been uploaded if there is a good place to place it

```html
<!DOCTYPE html>
<html lang="en">
<head>
<meta charset="utf-8">
<title>Breast Reconstruction — Pages 5 and 6</title>
<link rel="stylesheet" href="https://fonts.googleapis.com/css2?family=Questrial&display=swap">
<style>
  :root {
    --ink-black: #000000;
    --paper: #ffffff;
    --band: #fbf9fc;
    --header-text: #5a5a5a;
    --body-text: #8c8c8c;
    --accent-pink: #f095c1;
    --label-white: #ffffff;
  }
  * { margin: 0; padding: 0; box-sizing: border-box; }
  html, body {
    width: 1200px;
    height: 739px;
    overflow: hidden;
    background: var(--ink-black);
  }
  .spread-canvas {
    position: relative;
    width: 1200px;
    height: 739px;
    background: var(--ink-black);
    font-family: "Questrial", "Century Gothic", sans-serif;
  }
  .page-label {
    position: absolute;
    top: 82px;
    width: 120px;
    text-align: center;
    color: var(--label-white);
    font-size: 17px;
    letter-spacing: 0.3px;
  }
  .page-label--left { left: 215px; }
  .page-label--right { left: 789px; }

  .spread {
    position: absolute;
    left: 59px;
    top: 139px;
    width: 1036px;
    height: 518px;
    background: var(--paper);
  }
  .running-band {
    position: absolute;
    left: 0;
    top: 35px;
    width: 100%;
    height: 35px;
    background: var(--band);
  }
  .running-head {
    position: absolute;
    top: 43px;
    color: var(--header-text);
    font-size: 13.5px;
  }
  .running-head--left { left: 33px; }
  .running-head--right { left: 544px; }

  .procedure {
    position: absolute;
    width: 450px;
  }
  .procedure__title {
    color: var(--accent-pink);
    font-weight: 400;
    font-size: 21px;
    line-height: 1;
    margin-bottom: 17px;
  }
  .procedure__text {
    color: var(--body-text);
    font-size: 9.7px;
    line-height: 15px;
  }
  .procedure--lat { left: 33px; top: 149px; }
  .procedure--pap { left: 33px; top: 324px; }
  .procedure--implant { left: 544px; top: 151px; }
  .procedure--fat { left: 544px; top: 330px; }
</style>
</head>
<body>
<main class="spread-canvas">
  <div class="page-label page-label--left">Page 5</div>
  <div class="page-label page-label--right">Page 6</div>

  <section class="spread">
    <div class="running-band"></div>
    <p class="running-head running-head--left">Breast Reconstruction</p>
    <p class="running-head running-head--right">Breast Reconstruction</p>

    <article class="procedure procedure--lat">
      <h2 class="procedure__title">The Extended Latissimus Dorsi Muscle flap</h2>
      <p class="procedure__text">This surgery involves harvesting the latissimus dorsi muscle along with skin and fat from the back to reconstruct a breast. The latissimus dorsi muscle is the largest muscle in the back and responsible for extension and internal rotation of the shoulder joint. It is often used in various reconstructive procedures and does not result in any noticeable weakness. The patient will have a scar that is well hidden within the bra line. It is a more attractive option for patients who do not have enough abdominal tissue. The surgery is shorter and the recovery is faster than the DIEP flap reconstruction.</p>
    </article>

    <article class="procedure procedure--pap">
      <h2 class="procedure__title">The PAP flap</h2>
      <p class="procedure__text">The pap flap uses skin and fatty tissue from the inner upper thigh. The tissue is similar to the skin and fat removed in the cosmetic medial thigh lift procedure. This is a popular flap in woman who have had a prior tummy tuck or lack tissue in the abdomen. The amount of tissue that is supplied by the inner thigh tends to be less than there is available in most patients on the abdomen.</p>
    </article>

    <article class="procedure procedure--implant">
      <h2 class="procedure__title">Implant Base Reconstruction</h2>
      <p class="procedure__text">Implant base breast reconstruction is the most popular technique currently used in breast reconstruction. It is popular because the reconstruction results are excellent and the patients may return to work much faster than autologous breast reconstruction. The drawbacks are that it requires an implant and multiple surgeries. If a patient has radiation to the chest wall, implant base breast reconstruction will not be the best option due to higher rates of complications.</p>
    </article>

    <article class="procedure procedure--fat">
      <h2 class="procedure__title">Fat grafting</h2>
      <p class="procedure__text">Fat grafting is a great breast reconstruction technique to provide additional volume in an already reconstructed breast mound or correct contour deformity in a previous lumpectomy defect. The fat is harvested using a gentle suctioning technique and carefully injected into the breast to correct any contour deformity. There is no major scar associated with this technique.</p>
    </article>
  </section>
</main>
</body>
</html>
```